Product Designer Business Card

Small product design, engineering and prototyping firm in need of a clean, professional business card design. To support our 3D design and drawing services, we offer 3D printing, molding, and casting of plastics, silicones, resins, etc. Our logo can still be modified/changed if necessary. The red/orange color is preferred, but may be substituted with blue or green, potentially. Either way, the colour of the logo should be match/compliment colors used throughout the design. One thought is to have the logo/contact info on one side, with the other side describing services offered, like with a small icon of 3D printer, molding, casting, and computer with a 3D model on-screen.
Industry/Entity Type
Mechanical Engineering
Contact Information for Business Card
Company: Velkin Design
Phone: 613-555-0147
Email: marc@velkindesign.ca

```html
<!DOCTYPE html>
<html lang="en">
<head>
<meta charset="UTF-8">
<title>Velkin Design — Business Card</title>
<link rel="stylesheet" href="https://fonts.googleapis.com/css2?family=Roboto:wght@400;500;700&display=swap">
<style>
  :root {
    --page-bg: #e4e4e4;
    --card-white: #ffffff;
    --card-dark: #2e2e2e;
    --brand-red: #e0262a;
    --deep-maroon: #4a1414;
    --text-dark: #3a3a3a;
    --text-light: #ffffff;
    --rule: #5a2a2a;
  }
  * { box-sizing: border-box; margin: 0; padding: 0; }
  html, body {
    width: 1200px; height: 801px; overflow: hidden;
    background: var(--page-bg);
    font-family: "Roboto", Arial, sans-serif;
  }
  .stage {
    position: relative; width: 1200px; height: 801px;
    display: flex; align-items: center; justify-content: center; gap: 60px;
  }
  .card {
    position: relative; width: 520px; height: 300px;
    border-bottom: 4px solid var(--brand-red);
    box-shadow: 0 10px 24px rgba(0,0,0,0.18);
  }
  /* Front */
  .card-front { background: var(--card-white); }
  .brand-lockup {
    position: absolute; top: 48px; right: 36px;
    display: flex; align-items: center; gap: 12px;
  }
  .brand-dot {
    width: 34px; height: 34px; border-radius: 50%;
    background: var(--brand-red);
  }
  .brand-name {
    font-size: 30px; font-weight: 500; letter-spacing: 3px;
    color: var(--brand-red);
  }
  .top-rule {
    position: absolute; top: 120px; left: 250px; right: 30px;
    height: 1px; background: var(--rule);
  }
  .person {
    position: absolute; left: 34px; top: 168px;
  }
  .person-name {
    font-size: 22px; font-weight: 700; color: var(--brand-red);
  }
  .person-title {
    font-size: 15px; color: var(--text-dark); margin-top: 2px;
  }
  .person-rule {
    position: absolute; left: 34px; top: 226px; width: 190px;
    height: 1px; background: var(--rule);
  }
  .contact-list {
    position: absolute; left: 34px; top: 234px; list-style: none;
  }
  .contact-list li {
    display: flex; align-items: center; gap: 8px;
    font-size: 13px; color: var(--text-dark); line-height: 19px;
  }
  .contact-list svg { width: 12px; height: 12px; flex: none; }
  .contact-list .web-prefix { color: var(--text-dark); }
  .contact-list .web-domain { color: var(--brand-red); }

  /* Back */
  .card-back { background: var(--card-dark); }
  .back-brand {
    position: absolute; top: 78px; left: 0; right: 0;
    display: flex; align-items: center; justify-content: center; gap: 16px;
  }
  .back-brand .brand-dot { width: 44px; height: 44px; background: var(--text-light); }
  .back-brand .brand-name {
    font-size: 46px; font-weight: 400; letter-spacing: 8px; color: var(--text-light);
  }
  .services {
    position: absolute; top: 180px; left: 0; right: 0; text-align: center;
  }
  .services-heading {
    font-size: 19px; font-weight: 500; color: var(--brand-red);
    text-transform: uppercase; letter-spacing: 0.5px;
  }
  .services-list {
    margin-top: 10px; list-style: none;
    display: flex; justify-content: center; align-items: center; gap: 10px;
    font-size: 16px; color: var(--text-light);
  }
  .services-list .sep {
    width: 8px; height: 8px; border-radius: 50%; background: var(--brand-red);
  }
</style>
</head>
<body>
<main class="stage">
  <section class="card card-front" aria-label="Business card front">
    <div class="brand-lockup">
      <span class="brand-dot"></span>
      <span class="brand-name">Velkin Design</span>
    </div>
    <div class="top-rule"></div>
    <div class="person">
      <p class="person-name">Elias Moreau</p>
      <p class="person-title">Manager</p>
    </div>
    <div class="person-rule"></div>
    <ul class="contact-list">
      <li>
        <svg viewBox="0 0 24 24" aria-hidden="true"><path fill="#e0262a" d="M6.6 10.8a15 15 0 0 0 6.6 6.6l2.2-2.2a1 1 0 0 1 1-.25 11.4 11.4 0 0 0 3.6.57 1 1 0 0 1 1 1V20a1 1 0 0 1-1 1A17 17 0 0 1 3 4a1 1 0 0 1 1-1h3.5a1 1 0 0 1 1 1c0 1.25.2 2.45.57 3.6a1 1 0 0 1-.25 1z"/></svg>
        613-555-0147
      </li>
      <li>
        <svg viewBox="0 0 24 24" aria-hidden="true"><rect x="2" y="5" width="20" height="14" rx="1" fill="none" stroke="#e0262a" stroke-width="2"/><path d="M2 6l10 7 10-7" fill="none" stroke="#e0262a" stroke-width="2"/></svg>
        marc@velkindesign.ca
      </li>
      <li>
        <svg viewBox="0 0 24 24" aria-hidden="true"><circle cx="12" cy="12" r="10" fill="none" stroke="#e0262a" stroke-width="2"/><ellipse cx="12" cy="12" rx="4" ry="10" fill="none" stroke="#e0262a" stroke-width="2"/><path d="M2 12h20M4 7h16M4 17h16" stroke="#e0262a" stroke-width="1.5"/></svg>
        <span><span class="web-prefix">www.</span><span class="web-domain">velkindesign.ca</span></span>
      </li>
    </ul>
  </section>

  <section class="card card-back" aria-label="Business card back">
    <div class="back-brand">
      <span class="brand-dot"></span>
      <span class="brand-name">Velkin</span>
    </div>
    <div class="services">
      <h2 class="services-heading">Services Offered</h2>
      <ul class="services-list">
        <li>3D Printer</li>
        <li class="sep" aria-hidden="true"></li>
        <li>Molding</li>
        <li class="sep" aria-hidden="true"></li>
        <li>Casting</li>
        <li class="sep" aria-hidden="true"></li>
        <li>Computer</li>
      </ul>
    </div>
  </section>
</main>
</body>
</html>
```